Amber Ridge Dairy Business cards

We need a logo design for our family dairy. Included on the cards should be my name/my husbands name/the dairy name/ all the phone numbers/address and email. The name is Amber Ridge Dairy, LLC. We would like to use our farm mascot pic on the card. We know the pictures I sent you are of a beef cow but she is the mascot of the farm. We were thinking that maybe put a picture of her head in the middle of the card with a "A" on one side and a "D" on the other side with a "R" around the picture of the cow. But we are open to any ideas. We are looking for something kind of professional and a design that that can be used on cards, clothing and a car sign. Black lettering and blue for the other color...or what looks good.

Target Market(s)

All

Industry/Entity Type

Farming

Contact Information for Business Card

Rosa Pelton Owner (555)210-4471
Martin Strube Owner (555)382-9015
Amber Ridge Dairy, LLC (555)647-1238
Amberridgedairy@mailbox.example
7126 County Lane 14, Kewaskum, WI 53040

Font styles to use
Sans Serif

Colors
3176b5
3c7bb8
3277b5
0255a3

Requirements
Must have
• Some design that incorporates a drawing/pic of the cow pictures that were sent.
Nice to have
• no suggestions
Should not have
• no suggestions

```html
<!DOCTYPE html>
<html lang="en">
<head>
<meta charset="utf-8">
<title>Amber Ridge Dairy, LLC — Business Cards</title>
<link rel="stylesheet" href="https://fonts.googleapis.com/css2?family=Oswald:wght@700&family=Roboto:wght@400;500&display=swap">
<style>
  :root {
    --backdrop: #2e2e2e;
    --card: #ffffff;
    --ink: #111111;
    --muted: #1c1c1c;
    --brand-blue: #3176b5;
    --rule: #c9c9c9;
    --divider: #333333;
  }
  * { box-sizing: border-box; margin: 0; padding: 0; }
  html, body { width: 1200px; height: 900px; overflow: hidden; }
  body {
    background: var(--backdrop);
    position: relative;
    font-family: "Roboto", Arial, sans-serif;
    color: var(--ink);
  }
  .card {
    position: absolute;
    left: 317px;
    width: 580px;
    height: 345px;
    background: var(--card);
    border-radius: 18px;
    box-shadow: 0 4px 10px rgba(0,0,0,.45);
  }
  .card--front { top: 85px; }
  .card--back { top: 480px; }

  .wordmark {
    display: flex;
    align-items: center;
    gap: 12px;
    font-family: "Oswald", "Arial Narrow", sans-serif;
    font-weight: 700;
    color: var(--ink);
    text-transform: uppercase;
    letter-spacing: .5px;
  }
  .wordmark__dot {
    flex: none;
    border-radius: 50%;
    background: var(--brand-blue);
  }
  .card--front .wordmark {
    position: absolute;
    left: 0; right: 0;
    top: 148px;
    justify-content: center;
    font-size: 28px;
    line-height: 50px;
  }
  .card--front .wordmark__dot { width: 46px; height: 46px; }

  .card--back .wordmark {
    position: absolute;
    left: 30px;
    top: 138px;
    width: 240px;
    font-size: 21px;
    line-height: 1.15;
  }
  .card--back .wordmark__dot { width: 40px; height: 40px; }

  .divider {
    position: absolute;
    left: 282px;
    top: 68px;
    width: 2px;
    height: 207px;
    background: var(--divider);
  }
  .contacts {
    position: absolute;
    left: 324px;
    top: 78px;
    width: 206px;
  }
  .contact { padding-bottom: 4px; }
  .contact + .contact {
    border-top: 1px solid var(--rule);
    padding-top: 4px;
  }
  .contact__name { font-size: 17px; font-weight: 500; line-height: 22px; }
  .contact__role { font-size: 12.5px; line-height: 15px; color: var(--muted); }
  .contact__line {
    display: flex;
    align-items: center;
    gap: 4px;
    font-size: 14.5px;
    line-height: 20px;
    white-space: nowrap;
  }
  .contact__line svg { flex: none; width: 13px; height: 13px; }
  .contact__line--email { font-size: 12px; }

  .address {
    position: absolute;
    left: 0; right: 0;
    top: 302px;
    text-align: center;
    font-size: 12.5px;
  }
</style>
</head>
<body>
  <section class="card card--front" aria-label="Card front">
    <div class="wordmark"><span class="wordmark__dot"></span><span>Amber Ridge Dairy, LLC</span></div>
  </section>

  <section class="card card--back" aria-label="Card back">
    <div class="wordmark"><span class="wordmark__dot"></span><span>Amber Ridge Dairy, LLC</span></div>
    <div class="divider"></div>

    <div class="contacts">
      <div class="contact">
        <p class="contact__name">Rosa Pelton</p>
        <p class="contact__role">Owner</p>
        <p class="contact__line">
          <svg viewBox="0 0 13 13"><rect width="13" height="13" rx="2" fill="var(--brand-blue)"/><path d="M4 2.8l1.3 1.9-.8.9c.5 1.2 1.6 2.3 2.8 2.8l.9-.8 1.9 1.3-.8 1.4C6.6 10.2 2.8 6.4 2.7 3.6z" fill="#fff"/></svg>
          (555)210-4471
        </p>
      </div>
      <div class="contact">
        <p class="contact__name">Martin Strube</p>
        <p class="contact__role">Owner</p>
        <p class="contact__line">
          <svg viewBox="0 0 13 13"><rect width="13" height="13" rx="2" fill="var(--brand-blue)"/><path d="M4 2.8l1.3 1.9-.8.9c.5 1.2 1.6 2.3 2.8 2.8l.9-.8 1.9 1.3-.8 1.4C6.6 10.2 2.8 6.4 2.7 3.6z" fill="#fff"/></svg>
          (555)382-9015
        </p>
      </div>
      <div class="contact">
        <p class="contact__name">Amber Ridge Dairy, LLC</p>
        <p class="contact__line">
          <svg viewBox="0 0 13 13"><rect width="13" height="13" rx="2" fill="var(--brand-blue)"/><path d="M4 2.8l1.3 1.9-.8.9c.5 1.2 1.6 2.3 2.8 2.8l.9-.8 1.9 1.3-.8 1.4C6.6 10.2 2.8 6.4 2.7 3.6z" fill="#fff"/></svg>
          (555)647-1238
        </p>
        <p class="contact__line contact__line--email">
          <svg viewBox="0 0 13 13"><rect width="13" height="13" rx="2" fill="var(--brand-blue)"/><rect x="2.5" y="3.8" width="8" height="5.4" fill="#fff"/><path d="M2.5 3.8l4 3 4-3" fill="none" stroke="var(--brand-blue)" stroke-width=".9"/></svg>
          Amberridgedairy@mailbox.example
        </p>
      </div>
    </div>

    <p class="address">7126 County Lane 14, Ashford Falls, WI 53099</p>
  </section>
</body>
</html>
```